Book cover Design for her new book called 'Walking a path lit by courage and grace'

My name is Velarosha, I am the founder of The Quiet Lantern.
http://velarosha-wren.shopnestle.example/
My book is an inspirational story of love and triumphing from adversity. After 40 years of surviving a life full of sexual abuse, physical and mental abuse and living with the effects of poor self-esteem and post traumatic stress disorder, this book is a guide to help others navigate away from negative emotions and help them find their own light in life. With the techniques developed and described in the book The Quiet Lantern's mission is to empower people with the journey to their own hearts and create warmth, love and inspiration.
The colours in the website represent the softness that I love and I prefer flowers. The colour also can be soft as well as vibrant and feminine. The final design should represent healing, love, inspiration and passion.

Target Market(s)

Women over the age of 25 -80
Teenagers suffering from depression
Men and women suffering from poor self esteem
Woman who have poor self confidence.

Requirements
Should not have
• Should not be dark in colour or imagery.

```html
<!DOCTYPE html>
<html lang="en">
<head>
<meta charset="utf-8">
<title>Walking a path lit by courage and grace — Velarosha</title>
<link rel="stylesheet" href="https://fonts.googleapis.com/css2?family=Yellowtail&family=Damion&family=Cormorant+Garamond:ital,wght@1,700&display=block">
<style>
  :root {
    --stage: #9fb8b9;
    --teal-deep: #1f9ea3;
    --teal: #35b3b6;
    --teal-light: #62c4c3;
    --blossom: #f7f4f1;
    --blossom-pink: #f1cdd2;
    --branch: #8a6a5a;
    --title-pink: #f47a7f;
    --title-shadow: rgba(35, 35, 40, 0.6);
    --author-white: #ffffff;
  }
  html, body {
    margin: 0;
    padding: 0;
    width: 981px;
    height: 1200px;
    overflow: hidden;
    background: var(--stage);
  }
  .canvas {
    position: relative;
    width: 981px;
    height: 1200px;
  }
  .book-cover {
    position: absolute;
    left: 165px;
    top: 115px;
    width: 686px;
    height: 930px;
    overflow: hidden;
    box-shadow: 0 12px 30px rgba(0,0,0,0.2);
  }
  .cover-photo {
    position: absolute;
    inset: 0;
    background:
      radial-gradient(ellipse 120px 100px at 245px 90px, rgba(247,244,241,1), rgba(247,244,241,0) 75%),
      radial-gradient(ellipse 150px 110px at 480px 70px, rgba(247,244,241,0.9), rgba(247,244,241,0) 75%),
      radial-gradient(ellipse 150px 140px at 620px 190px, rgba(247,244,241,0.9), rgba(247,244,241,0) 75%),
      radial-gradient(ellipse 110px 110px at 110px 230px, rgba(247,244,241,0.85), rgba(247,244,241,0) 75%),
      radial-gradient(ellipse 120px 90px at 390px 340px, rgba(247,244,241,0.95), rgba(247,244,241,0) 75%),
      radial-gradient(ellipse 110px 90px at 200px 390px, rgba(247,244,241,0.95), rgba(247,244,241,0) 75%),
      radial-gradient(ellipse 120px 90px at 540px 380px, rgba(247,244,241,0.9), rgba(247,244,241,0) 75%),
      radial-gradient(ellipse 90px 110px at 90px 440px, rgba(241,205,210,0.85), rgba(241,205,210,0) 75%),
      radial-gradient(ellipse 110px 80px at 300px 450px, rgba(247,244,241,0.85), rgba(247,244,241,0) 75%),
      radial-gradient(ellipse 110px 90px at 600px 530px, rgba(247,244,241,0.9), rgba(247,244,241,0) 75%),
      radial-gradient(ellipse 60px 50px at 660px 370px, rgba(241,205,210,0.9), rgba(241,205,210,0) 75%),
      radial-gradient(ellipse 180px 220px at 560px 620px, rgba(31,140,150,0.55), rgba(31,140,150,0) 75%),
      radial-gradient(ellipse 260px 60px at 120px 120px, rgba(138,106,90,0.35), rgba(138,106,90,0) 75%),
      linear-gradient(180deg, var(--teal-light) 0%, var(--teal) 50%, var(--teal-deep) 100%);
  }
  .cover-title {
    position: absolute;
    left: 0;
    right: 0;
    top: 110px;
    margin: 0;
    text-align: center;
    font-family: "Yellowtail", "Damion", "Brush Script MT", "Segoe Script", cursive;
    font-weight: 400;
    font-size: 128px;
    line-height: 160px;
    color: var(--title-pink);
    text-shadow: 5px 7px 6px var(--title-shadow);
  }
  .cover-title span {
    display: block;
    white-space: nowrap;
  }
  .cover-author {
    position: absolute;
    left: 0;
    right: 0;
    bottom: 28px;
    margin: 0;
    text-align: center;
    font-family: "Cormorant Garamond", serif;
    font-style: italic;
    font-weight: 700;
    font-size: 42px;
    letter-spacing: 0.5px;
    color: var(--author-white);
  }
</style>
</head>
<body>
  <main class="canvas">
    <section class="book-cover">
      <div class="cover-photo" role="img" aria-label="Photograph of white and pale pink cherry blossom branches in a glass jar on a weathered turquoise wooden table"></div>
      <h1 class="cover-title">
        <span>Walking</span>
        <span>a path lit</span>
        <span>by courage</span>
        <span>and Grace</span>
      </h1>
      <p class="cover-author">Velarosha</p>
    </section>
  </main>
</body>
</html>
```